Vantor Ridge needs a Business Card Design

We need a business card design for an Information Technology company based in Fairfax Virginia called Vantor Ridge. We want the business card to use our logo colors. We need it to be double-sided. The business card needs to look professional but we would like it to be unique. You can get company information from our web site (http://www.vantorridgellc.example).

Target Market(s)

Target market is Government Agencies and Business Professionals.

Industry/Entity Type

Business

Requirements
Must have
• Must have section for company name, company address, company URL, employee name, title, phone and email. Also must have company logo and space for entering logos.

```html
<!DOCTYPE html>
<html lang="en">
<head>
<meta charset="utf-8">
<title>Vantor Ridge – Business Card</title>
<link rel="stylesheet" href="https://fonts.googleapis.com/css2?family=Arimo:wght@400;700&display=swap">
<style>
  :root {
    --navy: #2c3b91;
    --blue: #1877c4;
    --ink: #3a3f4a;
    --paper: #ffffff;
    --stage: #eceef1;
  }
  * { box-sizing: border-box; margin: 0; padding: 0; }
  html, body { width: 1200px; height: 784px; overflow: hidden; }
  body {
    background: var(--stage);
    font-family: "Arimo", Arial, sans-serif;
    position: relative;
  }
  .card {
    position: absolute;
    width: 540px;
    height: 310px;
    background: var(--paper);
    box-shadow: 0 6px 18px rgba(0,0,0,0.18);
    overflow: hidden;
  }

  /* Back side */
  .card-back { left: 60px; top: 90px; }
  .back-brand {
    position: absolute;
    left: 40px; top: 70px;
    display: flex; align-items: center; gap: 22px;
  }
  .back-mark {
    width: 110px; height: 110px;
    background: var(--navy);
  }
  .back-name {
    font-weight: 700;
    font-size: 48px;
    color: var(--blue);
    letter-spacing: 0.5px;
  }
  .back-url {
    position: absolute;
    right: 34px; bottom: 34px;
    font-size: 20px;
    color: var(--navy);
  }

  /* Front side */
  .card-front { left: 610px; top: 380px; }
  .holder {
    position: absolute;
    right: 30px; top: 22px;
    text-align: right;
    font-size: 12px;
    line-height: 1.3;
  }
  .holder-name { color: var(--ink); }
  .holder-title { color: var(--blue); }

  .brand {
    position: absolute;
    left: 30px; top: 80px;
    display: flex; align-items: center; gap: 14px;
  }
  .brand-mark { width: 50px; height: 50px; background: var(--navy); }
  .brand-name {
    font-weight: 700;
    font-size: 32px;
    color: var(--navy);
    line-height: 1;
  }
  .brand-tagline {
    margin-top: 4px;
    font-size: 8.5px;
    font-weight: 700;
    letter-spacing: 0.4px;
    text-transform: uppercase;
    color: var(--ink);
  }
  .rule-top {
    position: absolute;
    left: 300px; right: 0; top: 118px;
    height: 9px; background: var(--blue);
  }
  .rule-left {
    position: absolute;
    left: 0; width: 70px; top: 160px;
    height: 10px; background: var(--navy);
  }
  .rule-mid {
    position: absolute;
    left: 90px; right: 0; top: 160px;
    height: 10px; background: var(--blue);
  }

  .contacts {
    position: absolute;
    left: 70px; top: 180px;
    list-style: none;
  }
  .contacts li {
    display: flex; align-items: center; gap: 10px;
    height: 22px;
    font-size: 17px;
    color: var(--blue);
  }
  .contacts svg { width: 16px; height: 16px; fill: var(--navy); flex: none; }
</style>
</head>
<body>

<section class="card card-back" aria-label="Card back">
  <div class="back-brand">
    <div class="back-mark"></div>
    <div class="back-name">Vantor Ridge</div>
  </div>
  <div class="back-url">www.vantorridgellc.example</div>
</section>

<section class="card card-front" aria-label="Card front">
  <div class="holder">
    <div class="holder-name">Dana Merrow</div>
    <div class="holder-title">Manager</div>
  </div>

  <div class="brand">
    <div class="brand-mark"></div>
    <div>
      <div class="brand-name">Vantor Ridge</div>
      <div class="brand-tagline">Transforming Ideas into Solutions</div>
    </div>
  </div>

  <div class="rule-top"></div>
  <div class="rule-left"></div>
  <div class="rule-mid"></div>

  <ul class="contacts">
    <li>
      <svg viewBox="0 0 16 16" aria-hidden="true"><path d="M3 1l3 3-1.5 2a9 9 0 0 0 5.5 5.5L12 10l3 3-2 2C7 15 1 9 1 3z"/></svg>
      877.555.0142
    </li>
    <li>
      <svg viewBox="0 0 16 16" aria-hidden="true"><path d="M4 0h8v16H4z M5.5 2v10h5V2z"/></svg>
      165.555.0198
    </li>
    <li>
      <svg viewBox="0 0 16 16" aria-hidden="true"><path d="M4 1h8v4H4z M1 6h14v7h-3v2H4v-2H1z M5 10v4h6v-4z"/></svg>
      888.555.0176
    </li>
    <li>
      <svg viewBox="0 0 16 16" aria-hidden="true"><path d="M1 3h14v10H1z M2.5 4.5L8 9l5.5-4.5z" fill-rule="evenodd"/></svg>
      info@vantorridgellc.example
    </li>
    <li>
      <svg viewBox="0 0 16 16" aria-hidden="true"><path d="M8 1l7 7h-2v7H10v-5H6v5H3V8H1z"/></svg>
      1480 Meridian Ave, Suite 310
    </li>
  </ul>
</section>

</body>
</html>
```